Commercial Construction Interior Fitout company needs Logo and Business Cards

We need a logo and business card design. We specialise in Commercial Ceilings, Partitions, Plastering and Carpentry.

Company name: 7QX Commercial Interiors. Would like a professional looking card more than a fancy look. Gloss front preferably black pattern with Fluro Green and white text.

Will need:

Name
Position
Phone
Fax
Email
Postal Address
Web address
Updates

Thank you so much everyone for your efforts and fantastic designs..   If I didn't respond to everyone personally,  my apologises. 

Again, thanks all

R.M                               

Target Market(s)

Existing & New clients in the Construction Industry

Industry/Entity Type

Business

Requirements
Nice to have
• 7QX to be overlapped or made into some sort of Logo

```html
<!DOCTYPE html>
<html lang="en">
<head>
<meta charset="utf-8">
<title>7QX Commercial Interiors – Business Card</title>
<link rel="stylesheet" href="https://fonts.googleapis.com/css2?family=Open+Sans:wght@400;600;700&family=Roboto+Condensed:wght@500;700&display=swap">
<style>
  :root {
    --bg: #ebeceb;
    --card-dark: #2b2a29;
    --card-light: #ffffff;
    --green: #45b04a;
    --white: #ffffff;
    --ink: #2b2a29;
  }
  * { margin: 0; padding: 0; box-sizing: border-box; }
  html, body { width: 1048px; height: 1200px; overflow: hidden; }
  body { background: var(--bg); position: relative; font-family: "Open Sans", sans-serif; }

  .card {
    position: absolute;
    width: 753px;
    height: 434px;
    border-radius: 26px;
    overflow: hidden;
  }
  .card--front { left: 125px; top: 93px; background: var(--card-dark); }
  .card--back { left: 129px; top: 612px; background: var(--card-light); height: 433px; }

  /* Front */
  .front-brand {
    position: absolute; left: 78px; top: 58px;
    font-family: "Roboto Condensed", sans-serif; font-weight: 700;
    color: var(--white); line-height: 1;
  }
  .front-brand__mark { display: block; font-size: 78px; letter-spacing: 1px; }
  .front-brand__name { display: block; margin-top: 22px; font-size: 60px; letter-spacing: 0.5px; }

  .services {
    position: absolute; left: 78px; top: 245px; list-style: none;
    color: var(--white); font-size: 20px; line-height: 30px; letter-spacing: -0.3px;
  }
  .services li { position: relative; padding-left: 22px; }
  .services li::before {
    content: ""; position: absolute; left: 0; top: 13px;
    width: 6px; height: 6px; background: var(--green);
  }

  .pattern-area {
    position: absolute;
    background: linear-gradient(135deg, rgba(69,176,74,0.9), rgba(69,176,74,0.35) 60%, rgba(255,255,255,0.25));
    border-radius: 4px;
  }
  .card--front .pattern-area { left: 485px; top: 286px; width: 258px; height: 137px; }
  .card--back .pattern-area {
    left: 543px; top: 290px; width: 193px; height: 104px;
    background: linear-gradient(135deg, rgba(69,176,74,0.9), rgba(69,176,74,0.4) 60%, rgba(43,42,41,0.35));
  }

  /* Back */
  .back-header {
    position: absolute; left: 0; top: 0; width: 100%; height: 186px;
    background: var(--card-dark);
    border-bottom: 12px solid var(--green);
  }
  .holder { position: absolute; left: 115px; top: 97px; color: var(--white); }
  .holder__name { font-weight: 700; font-size: 24px; line-height: 32px; }
  .holder__position { font-weight: 400; font-size: 24px; line-height: 32px; }

  .back-brand {
    position: absolute; right: 72px; top: 34px; text-align: right;
    font-family: "Roboto Condensed", sans-serif; font-weight: 700;
    color: var(--white); line-height: 1;
  }
  .back-brand__mark { display: block; font-size: 68px; }
  .back-brand__name { display: block; margin-top: 18px; font-size: 27px; }

  .contacts { position: absolute; left: 107px; top: 217px; list-style: none; color: var(--ink); }
  .contacts li {
    display: flex; align-items: center; height: 37px;
    font-size: 21px; letter-spacing: 0.2px;
  }
  .contacts svg { width: 20px; height: 20px; margin-right: 13px; flex: none; }
</style>
</head>
<body>

<section class="card card--front" aria-label="Card front">
  <div class="front-brand">
    <span class="front-brand__mark">7QX</span>
    <span class="front-brand__name">COMMERCIAL INTERIORS</span>
  </div>
  <ul class="services">
    <li>COMMERCIAL CEILINGS</li>
    <li>PARTITIONS</li>
    <li>PLASTERING</li>
    <li>CARPENTRY</li>
  </ul>
  <div class="pattern-area" role="img" aria-label="Decorative pattern of green and white slanted tiles"></div>
</section>

<section class="card card--back" aria-label="Card back">
  <div class="back-header"></div>
  <div class="holder">
    <p class="holder__name">Your Name</p>
    <p class="holder__position">Position</p>
  </div>
  <div class="back-brand">
    <span class="back-brand__mark">7QX</span>
    <span class="back-brand__name">COMMERCIAL INTERIORS</span>
  </div>

  <ul class="contacts">
    <li>
      <svg viewBox="0 0 20 20" aria-hidden="true"><path d="M5 2l3 4-2 2c1 2.5 3 4.5 6 6l2-2 4 3-2 3C9 17 3 11 2 5z" fill="none" stroke="#2b2a29" stroke-width="1.6" stroke-linejoin="round"/></svg>
      012 345 6789
    </li>
    <li>
      <svg viewBox="0 0 20 20" aria-hidden="true"><rect x="5" y="2" width="10" height="6" fill="none" stroke="#2b2a29" stroke-width="1.5"/><rect x="2" y="8" width="16" height="9" rx="1" fill="none" stroke="#2b2a29" stroke-width="1.5"/><line x1="5" y1="13" x2="15" y2="13" stroke="#2b2a29" stroke-width="1.5"/></svg>
      023 456 7800
    </li>
    <li>
      <svg viewBox="0 0 20 20" aria-hidden="true"><rect x="2" y="5" width="16" height="11" fill="none" stroke="#2b2a29" stroke-width="1.5"/><path d="M2 5l8 6 8-6" fill="none" stroke="#2b2a29" stroke-width="1.5"/></svg>
      name@7qxmail.com
    </li>
    <li>
      <svg viewBox="0 0 20 20" aria-hidden="true"><path d="M10 18s-6-6-6-10a6 6 0 0 1 12 0c0 4-6 10-6 10z" fill="#2b2a29"/><circle cx="10" cy="8" r="2.2" fill="#fff"/></svg>
      Postal Address
    </li>
    <li>
      <svg viewBox="0 0 20 20" aria-hidden="true"><circle cx="10" cy="10" r="8" fill="none" stroke="#2b2a29" stroke-width="1.5"/><ellipse cx="10" cy="10" rx="3.5" ry="8" fill="none" stroke="#2b2a29" stroke-width="1.3"/><line x1="2" y1="10" x2="18" y2="10" stroke="#2b2a29" stroke-width="1.3"/></svg>
      www.7qx.com
    </li>
  </ul>

  <div class="pattern-area" role="img" aria-label="Decorative pattern of green and dark slanted tiles"></div>
</section>

</body>
</html>
```